Fashion Label Startup Business Card Design

Maribel Quint is a startup fashion designer based on the Gold Coast in QLD Australia. Maribels label " Vorine by Quint " is based upon taking old world design techniques and infusing them modern twist. The card design should incorporate an old world theme using colours like mustard, ocha, black, white and elements of lace pattern.

Card Details:

Maribel Quint
Fashion Designer
P: 04 0152 6847
E: vorinebyquint@mailbrook.com
W: www.friendsnet.com/VOrineByQuint

```html
<!DOCTYPE html>
<html lang="en">
<head>
<meta charset="utf-8">
<title>Maribel Quint — Fashion Designer Business Card</title>
<link rel="stylesheet" href="https://fonts.googleapis.com/css2?family=Libre+Baskerville:ital,wght@0,400;1,400&display=swap">
<style>
  :root {
    --card-brown: #5c3613;
    --card-brown-deep: #3f2208;
    --card-brown-light: #6b4119;
    --gold: #c9973c;
    --gold-soft: #d8b46c;
    --gold-muted: #b8893a;
  }
  html, body {
    margin: 0;
    padding: 0;
    width: 1200px;
    height: 768px;
    overflow: hidden;
    background: var(--card-brown-deep);
  }
  .business-card {
    position: relative;
    width: 1200px;
    height: 768px;
    overflow: hidden;
    font-family: "Libre Baskerville", "Times New Roman", serif;
    text-transform: uppercase;
  }
  .lace-texture {
    position: absolute;
    inset: 0;
    background:
      radial-gradient(ellipse at 50% 45%, var(--card-brown-light) 0%, var(--card-brown) 50%, var(--card-brown-deep) 100%);
  }
  .identity {
    position: absolute;
    left: 118px;
    top: 464px;
  }
  .designer-name {
    margin: 0;
    font-size: 44px;
    font-weight: 400;
    line-height: 1;
    letter-spacing: 0.36em;
    color: var(--gold);
  }
  .designer-role {
    margin: 10px 0 0;
    font-size: 31px;
    font-weight: 400;
    line-height: 1;
    letter-spacing: 0.3em;
    color: var(--gold-soft);
  }
  .contact-list {
    position: absolute;
    left: 118px;
    top: 594px;
    margin: 0;
    padding: 0;
    list-style: none;
    font-size: 21px;
    line-height: 29.5px;
    letter-spacing: 0.42em;
    color: var(--gold-soft);
  }
  .contact-item {
    display: flex;
    white-space: nowrap;
  }
  .contact-label {
    width: 78px;
    color: var(--gold-muted);
  }
  .contact-label--italic {
    font-style: italic;
  }
</style>
</head>
<body>
  <main class="business-card">
    <div class="lace-texture" role="img" aria-label="Old-world brown lace damask pattern background"></div>

    <header class="identity">
      <h1 class="designer-name">Maribel Quint</h1>
      <p class="designer-role">Fashion Designer</p>
    </header>

    <ul class="contact-list">
      <li class="contact-item"><span class="contact-label contact-label--italic">P:</span><span class="contact-value">04 0152 6847</span></li>
      <li class="contact-item"><span class="contact-label">E:</span><span class="contact-value">vorinebyquint@mailbrook.com</span></li>
      <li class="contact-item"><span class="contact-label">W:</span><span class="contact-value">www.friendsnet.com/VOrineByQuint</span></li>
    </ul>
  </main>
</body>
</html>
```